Harbourline wall and floor tiling

I would like you to design me a wrap for my work van, I will provide the logo I would like you to work off.
I’m happy for some slight little changes.
just need some creativity with the wrap design & background.
We are a tiling business in the construction industry.
Any designs are welcome but I do like what I have going on here and this type of font.
Show me what you got.
I would like the van to have a half wrap not just the side stickers like it shows in the photos.
The new mobile numbers I would like on the wrap are
0491528364
0412864159
We cover Tiling, screeding , waterproofing

Industry/Entity Type

Construction

Colors

Designer to choose colors to be used in the design.

Requirements
Must have
• Facebook & instagram logo somewhere small. Tiling, Waterproofing & Screeding

```html
<!DOCTYPE html>
<html lang="en">
<head>
<meta charset="utf-8">
<title>Harbourline Wall & Floor Tiling – Rear Van Wrap</title>
<link href="https://fonts.googleapis.com/css2?family=Bebas+Neue&family=Montserrat:wght@500;600;700&display=swap" rel="stylesheet">
<style>
  :root {
    --page: #ffffff;
    --wrap-white: #f4f4f4;
    --stripe-grey: #9a9a9a;
    --stripe-light: #d9d9d9;
    --brand-blue: #0a7ecb;
    --brand-blue-deep: #0570be;
    --logo-blue: #1a90dc;
    --icon-grey: #a3a3a3;
    --text-white: #ffffff;
  }
  * { margin: 0; padding: 0; box-sizing: border-box; }
  html, body {
    width: 1200px;
    height: 1200px;
    overflow: hidden;
    background: var(--page);
  }
  .canvas {
    position: relative;
    width: 1200px;
    height: 1200px;
  }
  .rear-wrap {
    position: absolute;
    left: 214px;
    top: 200px;
    width: 768px;
    height: 660px;
    border-radius: 36px 36px 14px 14px;
    overflow: hidden;
    background: var(--wrap-white);
  }
  .wrap-bands {
    position: absolute;
    inset: 0;
  }
  .brand-mark {
    position: absolute;
    left: 366px;
    top: 112px;
    width: 38px;
    height: 38px;
    background: var(--logo-blue);
    transform: rotate(45deg);
  }
  .brand-name {
    position: absolute;
    left: 0;
    width: 100%;
    top: 186px;
    text-align: center;
    font-family: "Montserrat", sans-serif;
    color: var(--logo-blue);
    text-transform: uppercase;
    line-height: 1.1;
  }
  .brand-name .brand-main {
    display: block;
    font-weight: 700;
    font-size: 56px;
    letter-spacing: 1px;
  }
  .brand-name .brand-sub {
    display: block;
    font-weight: 500;
    font-size: 27px;
    letter-spacing: 0.5px;
    margin-top: 6px;
  }
  .contact-block {
    position: absolute;
    left: 96px;
    top: 540px;
  }
  .phone-line {
    display: flex;
    align-items: center;
    gap: 10px;
  }
  .phone-icon { width: 42px; height: 42px; flex: none; }
  .phone-number {
    font-family: "Montserrat", sans-serif;
    font-weight: 600;
    font-size: 40px;
    color: var(--text-white);
    letter-spacing: 0.5px;
    line-height: 1;
  }
  .social-line {
    display: flex;
    align-items: center;
    gap: 8px;
    margin-top: 12px;
    padding-left: 2px;
    font-family: "Montserrat", sans-serif;
    font-weight: 600;
    font-size: 15px;
    color: var(--text-white);
  }
  .social-dot {
    width: 18px;
    height: 18px;
    border-radius: 50%;
    background: var(--icon-grey);
    flex: none;
  }
  .service-list {
    position: absolute;
    left: 494px;
    top: 504px;
    list-style: none;
  }
  .service-list li {
    display: flex;
    align-items: center;
    gap: 14px;
    height: 36px;
    font-family: "Bebas Neue", sans-serif;
    font-size: 32px;
    color: var(--text-white);
    letter-spacing: 0.3px;
  }
  .service-list li::before {
    content: "";
    width: 12px;
    height: 12px;
    background: var(--icon-grey);
    transform: rotate(45deg);
    flex: none;
  }
</style>
</head>
<body>
  <main class="canvas">
    <section class="rear-wrap" aria-label="Rear van wrap">
      <svg class="wrap-bands" width="768" height="660" viewBox="0 0 768 660" aria-hidden="true">
        <defs>
          <linearGradient id="blueBody" x1="0" y1="0" x2="0" y2="1">
            <stop offset="0" stop-color="#0a7ecb"/>
            <stop offset="1" stop-color="#0570be"/>
          </linearGradient>
        </defs>
        <polygon points="0,380 384,331 768,380 768,660 0,660" fill="#9a9a9a"/>
        <polygon points="0,396 384,345 768,396 768,660 0,660" fill="#d9d9d9"/>
        <polygon points="0,404 384,353 768,404 768,660 0,660" fill="url(#blueBody)"/>
      </svg>

      <span class="brand-mark" aria-hidden="true"></span>
      <h1 class="brand-name">
        <span class="brand-main">Harbourline</span>
        <span class="brand-sub">Wall &amp; Floor Tiling</span>
      </h1>

      <div class="contact-block">
        <div class="phone-line">
          <svg class="phone-icon" viewBox="0 0 42 42" aria-hidden="true">
            <circle cx="21" cy="21" r="21" fill="#a3a3a3"/>
            <path d="M14.5 10.5c1-.6 2-.3 2.6.6l2.2 3.6c.5.9.3 1.9-.5 2.5l-1.6 1.2c.9 2.3 2.7 4.3 5 5.4l1.3-1.5c.7-.8 1.7-.9 2.6-.4l3.5 2.3c.9.6 1.1 1.7.5 2.6l-1.4 2c-.8 1.1-2.2 1.6-3.5 1.2-6.6-2-11.6-7.3-13.3-14-.3-1.3.2-2.7 1.3-3.4z" fill="#ffffff"/>
          </svg>
          <span class="phone-number">0491-528-364</span>
        </div>
        <div class="social-line">
          <span class="social-dot" aria-hidden="true"></span>
          <span class="social-dot" aria-hidden="true"></span>
          <span class="social-handle">@harbourlinetiling</span>
        </div>
      </div>

      <ul class="service-list">
        <li>Tiling</li>
        <li>Screeding</li>
        <li>Waterproofing</li>
      </ul>
    </section>
  </main>
</body>
</html>
```